Falcrest security business card

Looking for a business card for my security company

Target Market(s)

Security

Industry/Entity Type

Security

Contact Information for Business Card

Name - Gil Marston. Title - General manager - direct 314 862.4490 website www. falcrestsecurityservices.example email - gil@ falcrestsecurityservices.example

Requirements
Must have
• Logo attached

```html
<!DOCTYPE html>
<html lang="en">
<head>
<meta charset="utf-8">
<title>Falcrest Security Services – Business Card</title>
<link href="https://fonts.googleapis.com/css2?family=Roboto:wght@400;700&display=swap" rel="stylesheet">
<style>
  :root {
    --backdrop: #3a3a3a;
    --card: #141414;
    --gold: #c9a040;
    --ink-light: #e6e6e6;
  }
  * { box-sizing: border-box; margin: 0; padding: 0; }
  html, body {
    width: 1200px; height: 801px; overflow: hidden;
    background: var(--backdrop);
    font-family: "Roboto", Arial, sans-serif;
  }
  .stage {
    position: relative; width: 1200px; height: 801px;
    display: flex; align-items: center; justify-content: center; gap: 60px;
  }
  .card {
    position: relative; width: 500px; height: 286px;
    background: var(--card);
    border-bottom: 2px solid var(--gold);
    border-right: 2px solid var(--gold);
    box-shadow: 0 12px 30px rgba(0,0,0,.45);
  }
  /* Front */
  .card-front { display: flex; align-items: center; padding: 0 36px; }
  .brand {
    width: 170px; text-align: center;
    font-weight: 700; font-size: 34px; letter-spacing: 1px;
    color: var(--gold); text-transform: uppercase;
  }
  .divider {
    width: 1px; height: 96px; background: var(--gold);
    margin: 0 18px 0 14px; align-self: center;
  }
  .details { color: var(--ink-light); }
  .person-name {
    font-weight: 700; font-size: 20px; color: var(--gold);
    text-transform: uppercase; letter-spacing: .3px;
  }
  .person-title { font-size: 14px; margin: 3px 0 10px; }
  .contact-list { list-style: none; font-size: 13px; line-height: 21px; }
  .contact-list li { display: flex; align-items: center; gap: 7px; white-space: nowrap; }
  .contact-icon { width: 11px; height: 11px; flex: none; fill: var(--gold); }
  /* Back */
  .card-back { display: flex; align-items: center; justify-content: center; }
  .back-brand {
    font-weight: 700; font-size: 34px; letter-spacing: 1px;
    color: var(--gold); text-transform: uppercase;
  }
</style>
</head>
<body>
<main class="stage">
  <section class="card card-front" aria-label="Business card front">
    <div class="brand">Falcrest</div>
    <div class="divider"></div>
    <div class="details">
      <p class="person-name">Gil Marston</p>
      <p class="person-title">General manager</p>
      <ul class="contact-list">
        <li>
          <svg class="contact-icon" viewBox="0 0 24 24"><path d="M6.6 10.8a15.2 15.2 0 0 0 6.6 6.6l2.2-2.2c.3-.3.7-.4 1-.2 1.1.4 2.3.6 3.6.6.6 0 1 .4 1 1V20c0 .6-.4 1-1 1A17 17 0 0 1 3 4c0-.6.4-1 1-1h3.5c.6 0 1 .4 1 1 0 1.3.2 2.5.6 3.6.1.3 0 .7-.2 1z"/></svg>
          314 862.4490
        </li>
        <li>
          <svg class="contact-icon" viewBox="0 0 24 24"><path d="M2 5h20v14H2z M2 5l10 8 10-8"/></svg>
          gil@ falcrestsecurityservices.example
        </li>
        <li>
          <svg class="contact-icon" viewBox="0 0 24 24"><path d="M12 2a10 10 0 1 0 0 20 10 10 0 0 0 0-20zm0 2c1.2 1.4 2 3.5 2.2 6H9.8C10 7.5 10.8 5.4 12 4zm-2.2 8h4.4c-.2 2.5-1 4.6-2.2 6-1.2-1.4-2-3.5-2.2-6z"/></svg>
          www. falcrestsecurityservices.example
        </li>
      </ul>
    </div>
  </section>
  <section class="card card-back" aria-label="Business card back">
    <p class="back-brand">Falcrest</p>
  </section>
</main>
</body>
</html>
```